2020-23 Strategic Plan - Graphic Design Work

We would would like to have our strategic plan designed. It should be two pages.

- I am looking for suggestions on ways to lay this out. I don’t like this boxy layout. It was great for the committee as we went through multiple versions, but I’d prefer the final not follow this boxy format

- I’ve included a few images we own (feel free to use any or none of them). Also attached our logo.

- Have a look at our new website to see our new branding look and feel (launching next week) https://thevorlex.plinthweb.com/

- I've included a copy of our logo.

Target Market(s)

Membership

Other font styles liked:
• Lato

Requirements
Must have
• Excellent layout. Easy to ready. Consistent with branding.

```html
<!DOCTYPE html>
<html lang="en">
<head>
<meta charset="utf-8">
<title>2020-2023 Strategic Plan</title>
<link href="https://fonts.googleapis.com/css2?family=Lato:wght@400;700;900&display=swap" rel="stylesheet">
<style>
  :root{
    --backdrop:#c3d4c2;
    --paper:#f0f0ee;
    --ink:#2b2b2b;
    --forest:#1d3f2a;
    --green-dark:#3b6b36;
    --green-mid:#5a9d4a;
    --green-olive:#96b56c;
    --green-soft:#b3d18e;
    --green-pale:#d6e3c0;
    --leaf:#8fbf5a;
    --red:#c8202f;
  }
  *{margin:0;padding:0;box-sizing:border-box}
  html,body{width:1200px;height:821px;overflow:hidden;background:var(--backdrop);font-family:'Lato',sans-serif;color:var(--ink)}
  .page{position:absolute;width:764px;height:1080px;background:var(--paper);transform:scale(.607);transform-origin:0 0;overflow:hidden;box-shadow:0 6px 14px rgba(0,0,0,.18)}
  .page--overview{left:82px;top:80px}
  .page--pillars{left:632px;top:81px}
  .page svg.shapes{position:absolute;left:0;top:0}
  .abs{position:absolute}

  .brand-name{font-family:'Lato',sans-serif;font-weight:900;color:var(--green-dark);text-align:center;line-height:1.15}
  .brand-name--cover{left:497px;top:121px;width:130px;font-size:14px}
  .brand-name--corner{left:580px;top:28px;width:150px;font-size:15px}

  .plan-title{left:27px;top:308px;font-size:27px;font-weight:900;color:var(--forest);letter-spacing:.2px}
  .plan-intro{left:27px;top:355px;font-size:15px;font-weight:700;line-height:19.6px;color:var(--forest)}

  .statement h2{font-size:20px;font-weight:700;color:var(--forest);margin-bottom:8px;letter-spacing:.3px}
  .statement p{font-size:15px;line-height:23.5px;color:var(--ink)}
  .statement--vision{left:172px;top:578px}
  .statement--mission{left:172px;top:705px}
  .statement--values{left:172px;top:888px}

  .headline{left:30px;top:14px;color:var(--red);font-weight:900;font-size:48px;letter-spacing:.5px}
  .headline small{font-size:15px;font-weight:700;letter-spacing:0}

  .pillar{left:466px;width:224px}
  .pillar h3{font-size:15px;font-weight:700;margin-bottom:8px;letter-spacing:.3px}
  .pillar p{font-size:10.5px;line-height:10.6px;margin-bottom:10px;color:#222}
  .pillar--educate{top:98px}.pillar--educate h3{color:var(--leaf)}
  .pillar--grow{top:204px}.pillar--grow h3{color:var(--green-olive)}
  .pillar--lead{top:330px}.pillar--lead h3{color:var(--green-mid)}
  .pillar--govern{top:445px}.pillar--govern h3{color:var(--green-dark)}

  .actions-title{left:31px;top:598px;color:var(--red);font-size:15px;font-weight:900}
  .actions{left:31px;list-style:none;font-size:14px;font-weight:700;line-height:26px;color:var(--forest)}
  .actions li{padding-left:12px;text-indent:-12px}
  .actions li::before{content:"\25CF";font-size:8px;margin-right:5px;vertical-align:2px}
  .actions--educate{top:626px}
  .actions--grow{top:722px}
  .actions--lead{top:848px}
  .actions--govern{top:944px}
</style>
</head>
<body>

<section class="page page--overview">
  <svg class="shapes" width="764" height="1080" viewBox="0 0 764 1080">
    <defs>
      <linearGradient id="crowdTone" x1="0" y1="0" x2="1" y2="0.3">
        <stop offset="0" stop-color="#b9aea4"/>
        <stop offset=".35" stop-color="#8c97a0"/>
        <stop offset=".6" stop-color="#7b8f88"/>
        <stop offset="1" stop-color="#3d6650"/>
      </linearGradient>
    </defs>
    <path role="img" aria-label="Photo of assessment professionals gathered at a member event" fill="url(#crowdTone)"
          d="M0,0H764V625C700,480 560,262 300,246C170,240 60,244 0,250Z"/>
    <path fill="#2f6344" opacity=".55" d="M490,0C610,120 710,330 764,625V0Z"/>
    <circle cx="562" cy="140" r="88" fill="#fff"/>
    <path d="M0,553H108V1043H0" fill="none" stroke="var(--green-dark)" stroke-width="4"/>
    <g class="icon-vision" transform="translate(110,617)">
      <circle r="35" fill="var(--forest)"/>
      <path d="M-20,0Q0,-16 20,0Q0,16 -20,0Z" fill="#fff"/>
      <circle r="7" fill="var(--red)"/><circle r="3" fill="#fff"/>
    </g>
    <g class="icon-mission" transform="translate(109,784)">
      <circle r="35" fill="var(--forest)"/>
      <circle r="13" fill="none" stroke="#fff" stroke-width="4"/>
      <circle r="4" fill="#fff"/>
      <path d="M0,0L15,-15" stroke="var(--red)" stroke-width="3"/>
      <path d="M12,-18L19,-19L18,-12" fill="none" stroke="var(--red)" stroke-width="3"/>
    </g>
    <g class="icon-values" transform="translate(111,951)">
      <circle r="35" fill="var(--forest)"/>
      <rect x="-16" y="-10" width="32" height="22" fill="#fff"/>
      <path d="M-6,-10V-15H6V-10" fill="none" stroke="var(--red)" stroke-width="3"/>
      <path d="M-8,-10V12M8,-10V12" stroke="var(--forest)" stroke-width="3"/>
    </g>
  </svg>

  <div class="abs brand-name brand-name--cover">VORLEX INSTITUTE<br>OF ASSESSORS</div>

  <h1 class="abs plan-title">2020-2023 STRAGETIC PLAN</h1>
  <p class="abs plan-intro">With over 1,250 members, the Vorlex Institute of Assessors<br>is Canada’s largest association of property assessment and taxation<br>professionals. Our diverse membership is comprised of individuals from<br>the private and public sectors practicing in the fields of assessment, consultan-<br>cy, appraisal, taxation and law. Incorporated in May 1957, the VIA is dedicated to<br>advancing the interests, education and professional competence of its members. Our<br>members are highly qualified and widely recognized as the leading professionals in the<br>property assessment industry.</p>

  <div class="abs statement statement--vision">
    <h2>VISION</h2>
    <p>To be the industry leader in education, ethical standards, and professional<br>accreditation in the field of property assessment in Canada.</p>
  </div>
  <div class="abs statement statement--mission">
    <h2>MISSION</h2>
    <p>To provide specialized education through a comprehensive approach to<br>training which embraces all available technologies. To promote profession-<br>al development and to ensure our members are recognized as experts in<br>the field of property assessment and related functions.</p>
  </div>
  <div class="abs statement statement--values">
    <h2>VALUES</h2>
    <p>The Vorlex Institute of Assessors and its members value profession-<br>alism, inclusivity, diversity, integrity, ethics, accountability, and expertise.<br>The VIA is committed to serving all members and stakeholders with com-<br>petence and respect, rejecting all forms of prejudice and discrimination.</p>
  </div>
</section>

<section class="page page--pillars">
  <svg class="shapes" width="764" height="1080" viewBox="0 0 764 1080" font-family="Lato, sans-serif">
    <defs>
      <linearGradient id="objectiveTone" x1="0" y1="0" x2="0" y2="1">
        <stop offset="0" stop-color="#d6e3c0"/>
        <stop offset=".35" stop-color="#a9c983"/>
        <stop offset=".6" stop-color="#6fa252"/>
        <stop offset="1" stop-color="#3b6b36"/>
      </linearGradient>
    </defs>
    <rect role="img" aria-label="Lightbulb illustration holding the four strategic objectives" x="58" y="112" width="242" height="400" rx="24" fill="url(#objectiveTone)"/>
    <text x="179" y="155" text-anchor="middle" font-size="15" font-weight="700" fill="#1d3f2a">OBJECTIVE</text>
    <text text-anchor="middle" font-size="8.5" fill="#2f4a22">
      <tspan x="179" y="192">Be the most trusted, relevant, and</tspan>
      <tspan x="179" y="202">accessible provider of education and</tspan>
      <tspan x="179" y="212">credentials in the field of property</tspan>
      <tspan x="179" y="222">assessment in Canada</tspan>
    </text>
    <text text-anchor="middle" font-size="8.5" fill="#24401a">
      <tspan x="179" y="262">Increase the VIA’s membership by</tspan>
      <tspan x="179" y="272">serving all career levels and forging</tspan>
      <tspan x="179" y="282">strong strategic partnerships.</tspan>
    </text>
    <text text-anchor="middle" font-size="8.5" fill="#fff">
      <tspan x="179" y="330">Strengthen the reputation of the</tspan>
      <tspan x="179" y="340">organization and its members by</tspan>
      <tspan x="179" y="350">acting as a leader within the field of</tspan>
      <tspan x="179" y="360">property assessment in Canada</tspan>
    </text>
    <text text-anchor="middle" font-size="8.5" fill="#fff">
      <tspan x="179" y="410">Fortify the future of the VIA</tspan>
      <tspan x="179" y="420">through operational excellence</tspan>
      <tspan x="179" y="430">and a diverse group of talented</tspan>
      <tspan x="179" y="440">volunteers</tspan>
    </text>
    <g fill="none" stroke="var(--red)" stroke-width="1.3" stroke-dasharray="4 3">
      <path d="M300,205H343V106H443"/>
      <path d="M300,272H389V211H443"/>
      <path d="M300,345H343V338H443"/>
      <path d="M300,425H314V454H443"/>
    </g>
    <g fill="var(--red)">
      <circle cx="443" cy="106" r="3"/><circle cx="443" cy="211" r="3"/>
      <circle cx="443" cy="338" r="3"/><circle cx="443" cy="454" r="3"/>
    </g>
    <g class="progress-bar">
      <path d="M725,584H764V632H725L697,608Z" fill="var(--green-pale)"/>
      <rect x="725" y="632" width="39" height="85" fill="var(--green-soft)"/>
      <rect x="725" y="717" width="39" height="122" fill="var(--green-olive)"/>
      <rect x="725" y="839" width="39" height="98" fill="var(--green-mid)"/>
      <rect x="725" y="937" width="39" height="143" fill="var(--green-dark)"/>
    </g>
  </svg>

  <h1 class="abs headline">STRATEGIC <small>PILLAR</small></h1>
  <div class="abs brand-name brand-name--corner">VORLEX INSTITUTE<br>OF ASSESSORS</div>

  <div class="abs pillar pillar--educate">
    <h3>EDUCATE</h3>
    <p>Ensure a catalogue of relevant, high-quality courses, which meet the evolving needs of assessment professionals</p>
    <p>Provide an equal VIA member experience and service, regardless of geography</p>
  </div>
  <div class="abs pillar pillar--grow">
    <h3>GROW</h3>
    <p>Enhance opportunities for senior assess-ment professionals through the FVIA designation.</p>
    <p>Connect with young professionals by en-hancing member onboarding, improv-ing member communications, and expanding scholarship opportunities.</p>
  </div>
  <div class="abs pillar pillar--lead">
    <h3>LEAD</h3>
    <p>Ensure a catalogue of relevant, high-quality courses, which meet the evolving needs of assessment professionals</p>
    <p>Provide an equal VIA member experience and service, regardless of geography</p>
  </div>
  <div class="abs pillar pillar--govern">
    <h3>GOVERN</h3>
    <p>Review and align association management practices with strategic objectives and statements of Vision, Mission and Values.</p>
    <p>Secure the VIA’s financial stability by re-viewing current pricing model and practic-ing sound risk management.</p>
  </div>

  <h2 class="abs actions-title">SAMPLE SUPPORTING ACTIONS</h2>
  <ul class="abs actions actions--educate">
    <li>Utilize technology to offer interactive and accessible online events</li>
    <li>Develop provincial legislation-specific content for VIA courses</li>
    <li>Lead opportunities for collaboration across districts to increase access to quality PD opportunities</li>
  </ul>
  <ul class="abs actions actions--grow">
    <li>Develop framework for a specialist designation track</li>
    <li>Work collaboratively with strategic partners from across the country to develop criteria for, and<br>launch, the FVIA designation</li>
    <li>Redesign the new member onboarding experience</li>
  </ul>
  <ul class="abs actions actions--lead">
    <li>Adopt an advocacy voice for the assessment profession to ensure interests are being represented</li>
    <li>Work with strategic partners to produce industry white papers with national relevance</li>
    <li>Engage with various levels of government across Canada</li>
  </ul>
  <ul class="abs actions actions--govern">
    <li>Align the VIA budget and staffing needs to achieve clear strategic objectives</li>
    <li>Utilize automation to modernize systems and administrative processes</li>
    <li>Review and assess the relevance of current committees to determine if sufficient to meet the<br>requirements of the strategic plan, and create new committees if deemed relevant</li>
  </ul>
</section>

</body>
</html>
```